Tui Netlink Website

We're looking for a basic website and order form for our stripped down ISP, Tui Netlink.

The front page should be basic with our two plan options - we're open to pretty much any design, but one possibility is an image of New Zealand with two clouds above it (similar to the quick mockup attached).

Clicking on one of the plans will then take the user to a basic order form.

We will also need a contact, about, and support page.

Industry/Entity Type

Isp

```html
<!DOCTYPE html>
<html lang="en">
<head>
<meta charset="utf-8">
<title>Tui Netlink — Pure Broadband</title>
<link href="https://fonts.googleapis.com/css2?family=Arimo:wght@400;700&family=Comfortaa:wght@700&family=Squada+One&display=swap" rel="stylesheet">
<style>
  :root {
    --white: #ffffff;
    --ink: #333333;
    --body-ink: #3a3a3a;
    --plan-blue: #1f66b0;
    --plan-purple: #7a3cc4;
    --icon-purple: #45287f;
    --account-bg: #5a2fb3;
    --footer-ink: #b9a8ef;
    --corner-blue: #1f6fb5;
  }
  * { margin: 0; padding: 0; box-sizing: border-box; }
  html, body { width: 1200px; height: 1040px; overflow: hidden; }
  body {
    position: relative;
    font-family: "Arimo", Arial, sans-serif;
    color: var(--white);
    background:
      radial-gradient(ellipse 420px 520px at 0px 60px, rgba(190,225,255,.85), transparent 70%),
      radial-gradient(ellipse 380px 420px at 1200px 0px, rgba(220,205,250,.9), transparent 70%),
      radial-gradient(ellipse 320px 420px at 1170px 380px, rgba(170,70,215,.85), transparent 70%),
      radial-gradient(ellipse 380px 380px at 60px 560px, rgba(20,140,210,.8), transparent 70%),
      linear-gradient(180deg, #5a5ee0 0%, #4d45d0 35%, #3a36b8 55%, #1d1f6a 80%, #07091f 100%);
  }
  .account-bar {
    position: absolute; left: 809px; top: 40px; width: 266px; height: 35px;
    background: var(--account-bg); border-radius: 3px;
    display: flex; align-items: center; font-size: 14px;
  }
  .account-bar a { color: var(--white); text-decoration: none; flex: 1; text-align: center; }
  .account-bar .divider { width: 1px; height: 18px; background: rgba(255,255,255,.5); }
  .brand { position: absolute; left: 138px; top: 66px; }
  .brand-name {
    font-family: "Comfortaa", sans-serif; font-weight: 700; font-size: 50px;
    line-height: 56px; color: var(--white); letter-spacing: -1px;
  }
  .brand-tagline {
    font-family: "Arimo", Arial, sans-serif; font-size: 12.5px; letter-spacing: .6px;
    margin-top: 4px; color: var(--white);
  }
  .main-nav {
    position: absolute; right: 127px; top: 118px; display: flex; gap: 22px;
    font-family: "Comfortaa", sans-serif; font-weight: 700; font-size: 16px;
  }
  .main-nav a { color: var(--white); text-decoration: none; }
  .hero-photo {
    position: absolute; left: 385px; top: 190px; width: 370px; height: 455px;
    border-radius: 46% 46% 40% 40%;
    background: radial-gradient(ellipse at 50% 45%, rgba(240,235,245,.55), rgba(40,40,70,.55) 60%, transparent 75%);
  }
  .plan { position: absolute; width: 300px; text-align: center; text-decoration: none; }
  .plan-left { left: 163px; top: 170px; }
  .plan-right { left: 740px; top: 170px; }
  .plan-cloud { position: absolute; left: 0; top: 0; }
  .plan-price {
    position: relative; font-family: "Squada One", sans-serif; padding-top: 36px;
    display: flex; justify-content: center; align-items: flex-end; gap: 6px;
  }
  .plan-price .amount { font-size: 68px; line-height: 60px; }
  .plan-price .period { font-size: 26px; line-height: 34px; }
  .plan-cta { position: relative; font-family: "Squada One", sans-serif; font-size: 20px; margin-top: 10px; letter-spacing: .5px; }
  .plan-left .plan-price, .plan-left .plan-cta { color: var(--plan-blue); }
  .plan-right .plan-price, .plan-right .plan-cta { color: var(--plan-purple); }
  .plan-speed { position: absolute; top: 162px; width: 100%; color: var(--white); font-size: 24px; }
  .plan-right .plan-speed { top: 166px; font-size: 25px; }
  .plan-speed strong { font-size: 1.17em; }
  .features {
    position: absolute; left: 138px; top: 613px; width: 933px; height: 331px;
    background: var(--white); border-radius: 4px; color: var(--ink);
  }
  .feature { position: absolute; top: 57px; }
  .feature-icon { display: block; margin: 0 auto; height: 84px; }
  .feature-title { font-size: 18px; font-weight: 700; line-height: 22px; text-align: center; margin-top: 10px; }
  .feature-text { font-size: 14px; line-height: 17px; color: var(--body-ink); margin-top: 16px; }
  .feature-video { left: 44px; width: 215px; }
  .feature-speed { left: 353px; width: 245px; }
  .feature-peak { left: 686px; width: 225px; }
  .hotline {
    position: absolute; top: 983px; width: 100%; text-align: center;
    font-size: 17.5px; color: var(--footer-ink);
  }
  .hotline strong { color: var(--white); }
  .corner-mark { position: absolute; left: 0; bottom: 0; width: 50px; height: 16px; background: var(--corner-blue); }
</style>
</head>
<body>
  <nav class="account-bar">
    <a href="#">My Account</a><span class="divider"></span><a href="#">Order Now</a>
  </nav>

  <header class="brand">
    <div class="brand-name">tui netlink</div>
    <div class="brand-tagline">PURE BROADBAND. PURE SPEED. NO LIMITS</div>
  </header>

  <nav class="main-nav">
    <a href="#">home</a><a href="#">products</a><a href="#">promos</a>
    <a href="#">pricing</a><a href="#">support</a><a href="#">contact</a>
  </nav>

  <div class="hero-photo" role="img" aria-label="Photo of a young woman sitting cross-legged using a laptop, wearing headphones and a cap"></div>

  <a class="plan plan-left" href="#">
    <svg class="plan-cloud" width="290" height="160" viewBox="0 0 290 160" aria-hidden="true">
      <g fill="#fff">
        <circle cx="60" cy="95" r="52"/><circle cx="115" cy="55" r="50"/>
        <circle cx="180" cy="50" r="45"/><circle cx="235" cy="90" r="52"/>
        <circle cx="150" cy="105" r="50"/><rect x="60" y="70" width="175" height="85" rx="40"/>
      </g>
    </svg>
    <div class="plan-price"><span class="amount">$95</span><span class="period">/month</span></div>
    <div class="plan-cta">CLICK HERE TO ORDER</div>
    <div class="plan-speed">up to <strong>30mbps</strong> down</div>
  </a>

  <a class="plan plan-right" href="#">
    <svg class="plan-cloud" width="290" height="160" viewBox="0 0 290 160" aria-hidden="true">
      <g fill="#fff">
        <circle cx="60" cy="95" r="52"/><circle cx="115" cy="55" r="50"/>
        <circle cx="180" cy="50" r="45"/><circle cx="235" cy="90" r="52"/>
        <circle cx="150" cy="105" r="50"/><rect x="60" y="70" width="175" height="85" rx="40"/>
      </g>
    </svg>
    <div class="plan-price"><span class="amount">$99</span><span class="period">/month</span></div>
    <div class="plan-cta">CLICK HERE TO ORDER</div>
    <div class="plan-speed">up to <strong>100mbps</strong> down</div>
  </a>

  <section class="features">
    <article class="feature feature-video">
      <svg class="feature-icon" width="104" height="80" viewBox="0 0 104 80" aria-hidden="true">
        <rect x="0" y="2" width="102" height="76" rx="3" fill="#45287f"/>
        <g fill="#fff">
          <rect x="10" y="7" width="9" height="7"/><rect x="28" y="7" width="9" height="7"/><rect x="46" y="7" width="9" height="7"/><rect x="64" y="7" width="9" height="7"/><rect x="82" y="7" width="9" height="7"/>
          <rect x="10" y="66" width="9" height="7"/><rect x="28" y="66" width="9" height="7"/><rect x="46" y="66" width="9" height="7"/><rect x="64" y="66" width="9" height="7"/><rect x="82" y="66" width="9" height="7"/>
          <rect x="8" y="19" width="86" height="42"/>
        </g>
        <circle cx="51" cy="40" r="16" fill="none" stroke="#45287f" stroke-width="4"/>
        <path d="M45 31 L59 40 L45 49 Z" fill="#45287f"/>
      </svg>
      <h3 class="feature-title">Crystal Clear High<br>Definition Video</h3>
      <p class="feature-text">With a network especially engineered for smooth streaming performance, enjoy HD videos as they load and play amazingly fast.</p>
    </article>
    <article class="feature feature-speed">
      <svg class="feature-icon" width="106" height="80" viewBox="0 0 106 80" aria-hidden="true">
        <rect x="9" y="2" width="88" height="66" rx="3" fill="#45287f"/>
        <rect x="17" y="10" width="72" height="48" fill="#fff"/>
        <path d="M0 70 H106 V77 Q106 80 103 80 H3 Q0 80 0 77 Z" fill="#45287f"/>
        <rect x="44" y="70" width="18" height="3" fill="#fff"/>
        <path d="M43 20 L43 42 L48 37 L53 46 L57 44 L52 35 L59 34 Z" fill="#45287f"/>
      </svg>
      <h3 class="feature-title">Ultra-Fast Speeds<br>Across Multiple Devices</h3>
      <p class="feature-text">100mbps enables a whole family on tablets, laptops, desktops and smart TVs to watch online videos, game, surf and download at ultra-fast speeds.</p>
    </article>
    <article class="feature feature-peak">
      <svg class="feature-icon" width="84" height="84" viewBox="0 0 84 84" aria-hidden="true">
        <circle cx="42" cy="42" r="40" fill="#45287f"/>
        <circle cx="42" cy="42" r="32" fill="#fff"/>
        <circle cx="42" cy="42" r="29" fill="none" stroke="#45287f" stroke-width="2"/>
        <g stroke="#45287f" stroke-width="2">
          <line x1="42" y1="15" x2="42" y2="20"/><line x1="42" y1="64" x2="42" y2="69"/>
          <line x1="15" y1="42" x2="20" y2="42"/><line x1="64" y1="42" x2="69" y2="42"/>
        </g>
        <path d="M42 20 V42 H26" fill="none" stroke="#45287f" stroke-width="4"/>
        <circle cx="42" cy="42" r="4" fill="#45287f"/>
      </svg>
      <h3 class="feature-title">Superior Peak Hour<br>Performance</h3>
      <p class="feature-text">Only Tui Netlink prioritises different types of traffic, allowing streaming, surfing or gaming to run seamlessly all the time.</p>
    </article>
  </section>

  <p class="hotline">Questions? Call our 24/7 hotline <strong>6420 5180</strong> or visit one of our retail outlets.</p>
  <div class="corner-mark"></div>
</body>
</html>
```